Salon Vireau

menu design, menu change,
will send hand written rough draft soon

Reason: Got off to a slow start. Things are progressing now. Thank you.

Target Market(s)

18-60 yr olds, blue collar & professionals, middle class, median income, families,upscale - casual- steakhouse concept

Industry/Entity Type

Restaurant

Colors
f68d4c
f37122
f78f20
faa54b
ffc214
fece3e
fbee3e
fbed22
333333

Requirements
Must have
• Front cover, back cover. 2 inside views
Nice to have
• 8 x 14 page size

```html
<!DOCTYPE html>
<html lang="en">
<head>
<meta charset="utf-8">
<title>Salon Vireau — Menu</title>
<link href="https://fonts.googleapis.com/css2?family=Raleway:ital,wght@0,300;0,400;0,600;0,700;1,300;1,400&display=swap" rel="stylesheet">
<style>
  :root{
    --page:#ffffff;
    --board:#33302f;
    --gold:#c9a66b;
    --ink:#d9d4cc;
    --dark:#2a2726;
  }
  *{margin:0;padding:0;box-sizing:border-box}
  html,body{width:1200px;height:1000px;overflow:hidden;background:var(--page)}
  body{font-family:"Raleway",sans-serif;position:relative}
  .menu{position:absolute;left:83px;top:205px;width:1034px;height:590px;background:var(--board)}
  .menu > *{position:absolute}
  .section-title{font-weight:300;color:var(--gold);font-size:23px;line-height:1;white-space:nowrap}
  .section-note{font-size:6.5px;color:var(--ink);text-transform:uppercase;letter-spacing:.2px;white-space:nowrap}
  .item h3{font-weight:300;color:var(--gold);font-size:13px;line-height:1.1}
  .item p.desc{font-style:italic;font-weight:300;color:var(--ink);font-size:6.3px;line-height:1.3}
  .item p.price{font-weight:300;color:var(--ink);font-size:7.5px;margin-top:1px}
  .rule{height:2px;background:var(--gold)}
  .rule-dashed{height:0;border-top:1.5px dashed #ffffff}
  .sides-box{border:2px solid var(--gold)}
  .box-head{border:1.5px solid var(--gold);color:var(--gold);font-weight:300;text-align:center}
  .side-list{list-style:none;color:var(--ink);font-size:6.5px;line-height:1.35;font-weight:300}
  .potato-list{list-style:none;color:var(--ink);font-size:7.5px;line-height:1.35;font-weight:300}
  .potato-list li::before{content:"";display:inline-block;width:6px;height:6px;background:var(--gold);margin-right:5px}
  .advisory{background:var(--gold);color:var(--dark);font-weight:700;font-size:6px;line-height:18px;padding-left:12px;letter-spacing:.1px;white-space:nowrap}
  .brand{color:var(--gold);font-weight:400;font-size:22px;white-space:nowrap}
</style>
</head>
<body>
<main class="menu">

  <!-- Cattle Country -->
  <h2 class="section-title" style="left:16px;top:10px">This is Cattle Country!</h2>
  <p class="section-note" style="left:17px;top:37px">All served with choice of potato &amp; hot bread</p>

  <div class="item" style="left:17px;top:51px;width:225px"><h3>Chicken Fried Steak</h3><p class="desc">Hand breaded &amp; served with Country Gravy</p><p class="price">12.99</p></div>
  <div class="item" style="left:262px;top:51px;width:240px"><h3>Mushroom Ground Sirloin Steak</h3><p class="desc">14 oz ground sirloins smothered with beef mushroom gravy</p><p class="price">12.99</p></div>
  <div class="rule-dashed" style="left:10px;top:88px;width:497px"></div>
  <div class="item" style="left:17px;top:92px;width:225px"><h3>Parmesian Pepper Press Steak</h3><p class="desc">12 oz choice tenderloin cut, charbroiled &amp; coated with a Parmesian Pepper Crust</p><p class="price">19.99</p></div>
  <div class="item" style="left:262px;top:92px;width:240px"><h3>Steak Dei Rio</h3><p class="desc">12 oz choice tenderloin cut rubbed with bold Southwestern spices, flame broiled, topped with chili pepper butter &amp; fried onion tanglers</p><p class="price">19.99</p></div>
  <div class="item" style="left:17px;top:137px;width:225px"><h3>Steak Chateau Briand</h3><p class="desc">12 oz choice tenderloin cut, drizzeled with a parmesian cream sauce &amp; complimented with grilled asparagus spears</p><p class="price">19.99</p></div>
  <div class="item" style="left:262px;top:137px;width:240px"><h3>Boston Bleau Cheese Steak</h3><p class="desc">12 oz choice tenderloin cut, flamebroiled, topped with melting bleu cheese crumbles</p><p class="price">19.99</p></div>
  <div class="rule" style="left:7px;top:182px;width:496px"></div>

  <!-- Premium -->
  <h2 class="section-title" style="left:15px;top:189px">Vireau Premium Steak Selections</h2>
  <p class="section-note" style="left:17px;top:213px">- Choice and prime grade beef - served with house salad, choice of potato &amp; hot bread</p>
  <div class="item" style="left:17px;top:229px;width:225px"><h3>Filet Mignon</h3><p class="desc">Bacon wrapped,the most tender cut</p><p class="price">(8oz) 24.99 &nbsp;&nbsp; (10oz) 28.99</p></div>
  <div class="item" style="left:262px;top:229px;width:240px"><h3>Ribeye Steak</h3><p class="desc">Well marbeled, rich, full of flavor cut from the prime rib</p><p class="price">(15oz) 28.99</p></div>
  <div class="item" style="left:17px;top:266px;width:225px"><h3>Kansas City Strip</h3><p class="desc">Firmer texture, full of flavor</p><p class="price">(16oz) 26.99</p></div>
  <div class="item" style="left:262px;top:266px;width:240px"><h3>Beef Tenderloin Ka-Bob</h3><p class="desc">8 oz beef tenderloin, skewered with bell peppers, onions, tomatoes, mushrooms, pineapple &amp; drizzled with a light Italian marinade</p><p class="price">(8 oz) 26.99</p></div>
  <div class="rule" style="left:10px;top:311px;width:507px"></div>

  <!-- Chicken & Seafood -->
  <h2 class="section-title" style="left:16px;top:316px">Chicken &amp; Seafood</h2>
  <p class="section-note" style="left:17px;top:341px">Served with choice of potato &amp; hot bread</p>
  <div class="item" style="left:17px;top:360px;width:215px"><h3>Charbroiled Chicken Breast</h3><p class="desc">10 oz flame broiled breast</p><p class="price">14.99</p></div>
  <div class="item" style="left:17px;top:397px;width:215px"><h3>Fried Chicken Breast</h3><p class="desc">10 oz handbreaded breast, fried, served with corn on the cob, mashed potatoes &amp; country gravy</p><p class="price">14.99</p></div>
  <div class="item" style="left:17px;top:443px;width:215px"><h3>Hand Breaded Chicken Strips</h3><p class="desc">Cut &amp; breaded per order</p><p class="price">9.99</p></div>
  <div class="item" style="left:17px;top:480px;width:215px"><h3>Chicken Ka-Bob</h3><p class="desc">10 oz charbroiled breast, skewered with bell peppers, onions, mushrooms, tomatoes, pineapple, and drizzled with light Italian marinade</p><p class="price">19.99</p></div>
  <div class="item" style="left:17px;top:532px;width:215px"><h3>North Atlantic Salmon</h3><p class="desc">Charbroiled fillet 8 oz</p><p class="price">19.99</p></div>
  <div class="item" style="left:262px;top:361px;width:125px"><h3>English Style Cod</h3><p class="desc">House battered Icelandic Cod loins</p><p class="price">17.99</p></div>
  <div class="item" style="left:262px;top:398px;width:125px"><h3>Deep Fried Gulf Shrimp</h3><p class="desc">6 jumbo shrimp</p><p class="price">17.99</p></div>
  <div class="item" style="left:262px;top:450px;width:125px"><h3>Mahi Mahi</h3><p class="desc">9 oz charbroiled served under a shrimp &amp; mushroom white sauce on a bed of steamed garden vegetables</p><p class="price">19.99</p></div>
  <div class="item" style="left:262px;top:511px;width:125px"><h3>Country Fried Catfish</h3><p class="desc">Catfish fillets, hand broiled &amp; deep fried</p><p class="price">17.99</p></div>

  <!-- Sides -->
  <div class="sides-box" style="left:392px;top:311px;width:116px;height:254px"></div>
  <div class="box-head" style="left:396px;top:319px;width:108px;height:32px;font-size:21px;line-height:30px">Sides</div>
  <ul class="side-list" style="left:400px;top:358px;width:104px">
    <li>- Steamed Garden<br>&nbsp;&nbsp;Vegetables &nbsp;4.99</li>
    <li>- Twice Baked Potato &nbsp;4.99</li>
    <li>- Loaded Baked &amp; Mashed<br>&nbsp;&nbsp;Potato &nbsp;4.99</li>
    <li>- Grilled Asparagus &nbsp;4.99</li>
    <li>- House Or Caesar Salad &nbsp;4.99</li>
    <li style="margin-top:4px;font-style:italic">*If in place of potato, add 2.99</li>
  </ul>
  <div class="box-head" style="left:396px;top:451px;width:108px;height:28px;font-size:13px;line-height:26px">Potato Choice</div>
  <ul class="potato-list" style="left:401px;top:492px;width:100px">
    <li>Baked</li><li>Mashed</li><li>American Fries</li><li>German Fries</li><li>French Fries</li><li>Onion Rings</li>
  </ul>

  <p class="advisory" style="left:0;top:572px;width:517px;height:18px">CONSUMER ADVISORY: CONSUMING RAW OR UNDER COOKED MEAT, POULTRY, SEAFOOD, SHELLFISH, OR EGGS MAY INCREASE YOUR RISK OF FORBORNE ILLNESS</p>

  <!-- Appetizers -->
  <h2 class="section-title" style="left:532px;top:10px">Appetizers</h2>
  <div class="item" style="left:532px;top:51px;width:235px"><h3>Fried Mozzarella Cheese Sticks</h3><p class="desc">Hand breaded sticks served with marinara sauce</p><p class="price">8.99</p></div>
  <div class="item" style="left:532px;top:88px;width:235px"><h3>French Fried Pickles</h3><p class="desc">Basket full of house breaded pickles with ranch dressing</p><p class="price">8.99</p></div>
  <div class="item" style="left:532px;top:125px;width:235px"><h3>Onion Ring Tower</h3><p class="price">8.99</p></div>
  <div class="item" style="left:532px;top:154px;width:235px"><h3>Cheddar Cheese Jalapeno Peppers</h3><p class="desc">Fried cheddar cheese stuffed jalapenos with ranch dressing (10)</p><p class="price">9.99</p></div>
  <div class="item" style="left:532px;top:192px;width:235px"><h3>Calamari</h3><p class="desc">Hand breaded &amp; served with cocktail sauce</p><p class="price">12.99</p></div>
  <div class="item" style="left:532px;top:229px;width:235px"><h3>Shrimp Cocktail</h3><p class="desc">10 chilled shrimp with cocktail sauce</p><p class="price">11.99</p></div>
  <div class="item" style="left:532px;top:266px;width:235px"><h3>Macha Nachos</h3><p class="desc">Corn tortilla chips, refried beans, taco meat, chili, cheese, salsa, lettuce, tomato, jalapenos &amp; sour cream</p><p class="price">9.99</p></div>
  <div class="item" style="left:532px;top:311px;width:235px"><h3>Rocky Mountain Oysters</h3><p class="desc">Full pound of breaded &amp; fried oysters served with homemade sauce</p><p class="price">12.99</p></div>
  <div class="rule" style="left:525px;top:358px;width:250px"></div>

  <!-- Burgers -->
  <h2 class="section-title" style="left:531px;top:371px">Gourmet Burgers</h2>
  <p class="section-note" style="left:532px;top:396px">All served with bottleneck fries</p>
  <div class="item" style="left:532px;top:416px;width:105px"><h3>Vireau Burger</h3><p class="desc">Cheddar cheese, smoked ham, more cheese &amp; bacon</p><p class="price">9.99</p></div>
  <div class="item" style="left:647px;top:416px;width:125px"><h3>Great Western</h3><p class="desc">Cheddar cheese, bacon, onion rings &amp; Hollis's BBQ sauce</p><p class="price">9.99</p></div>
  <div class="item" style="left:532px;top:467px;width:105px"><h3>Swiss Mushroom</h3><p class="desc">Swiss cheese, bacon, sauteed mushrooms</p><p class="price">9.99</p></div>
  <div class="item" style="left:647px;top:467px;width:125px"><h3>Ranch House<br>Burger</h3><p class="desc">Cheddar cheese, bacon &amp; a fried egg</p><p class="price">9.99</p></div>
  <div class="item" style="left:532px;top:517px;width:105px"><h3>Bacon Cheddar</h3><p class="desc">Cheddar cheese, bacon on a Brioche bun</p><p class="price">9.99</p></div>
  <div class="item" style="left:647px;top:524px;width:125px"><h3>Fire House Burger</h3><p class="desc">Pepper Jack cheese, bacon, grilled onions, jalapenos &amp; hot buffalo sauce</p><p class="price">9.99</p></div>

  <!-- Salads -->
  <h2 class="section-title" style="left:785px;top:10px">Salads</h2>
  <div class="item" style="left:785px;top:51px;width:245px"><h3>Classic Chef Salad</h3><p class="desc">Tossed iceburg lettuce, cheese, tomato, cucumber, egg, ham, turkey, bacon, croutons and a garlic breadstick</p><p class="price">9.99</p></div>
  <div class="item" style="left:785px;top:96px;width:245px"><h3>Blackaned Chicken Southwest Salad</h3><p class="desc">Blackened chicken served over iceburg lettuce, cheese, tomato, sweet corn, black beans, black olives, avocados, sour cream, tortilla chips, and Southwest dressing</p><p class="price">9.99</p></div>
  <div class="item" style="left:785px;top:149px;width:245px"><h3>West Coast Berry Salad</h3><p class="desc">Romaine lettuce, black cheese, egg, tomato, black &amp; blue berries, strawberry, pineapple, oranges, almonds, candried walnuts, cranberries, croutons &amp; raspberry vinaigrette, chicken or shrimp</p><p class="price">9.99</p></div>
  <div class="item" style="left:785px;top:202px;width:245px"><h3>Chicken Salad</h3><p class="desc">Fried or charbroiled chicken over iceburg lettuce, cheese, egg, tomato, cucumber, bacon, croutons &amp; a garlic breadstick</p><p class="price">9.99</p></div>
  <div class="item" style="left:785px;top:247px;width:245px"><h3>Caprese Salad</h3><p class="desc">Fresh baby spinach, fresh mozzarella, tomato, balsamic vinegar, basil</p><p class="price">9.99</p></div>
  <div class="rule" style="left:783px;top:287px;width:244px"></div>

  <!-- Sandwiches -->
  <h2 class="section-title" style="left:783px;top:299px">Signature Sandwiches</h2>
  <div class="item" style="left:785px;top:330px;width:112px"><h3>Turkey Avocado<br>Cream Cheese</h3><p class="desc">Smoked turkey, lettuce, tomato, cucumber, avocados, cream cheese, and honey mustard on a warm Ciabatta bun</p><p class="price">9.99</p></div>
  <div class="item" style="left:909px;top:330px;width:115px"><h3>3 Layer Reuben</h3><p class="desc">Corned beef, kraut, Swiss &amp; cheddar cheese, 1000 island sauce layered in 3 grilled slices of marble</p><p class="price">9.99</p></div>
  <div class="item" style="left:785px;top:411px;width:112px"><h3>French Dip</h3><p class="desc">Slow roasted, shaved, beef, provolone cheese, red onion slices, on a 12" Hogie with Aujus</p><p class="price">9.99</p></div>
  <div class="item" style="left:909px;top:396px;width:115px"><h3>Chicken Club<br>Sandwich</h3><p class="desc">Hand breaded chicken breast, provolone cheese, bacon, lettuce, tomato, pickle all on Brioche bun</p><p class="price">9.99</p></div>
  <div class="item" style="left:785px;top:469px;width:112px"><h3>Classic Clubhouse<br>Sandwich</h3><p class="desc">Ham, turkey, lettuce, tomato, pickle, onion, bacon, cheddar &amp; Swiss cheese, 2 sauces, layered in 3 toasted country style bread slices</p><p class="price">9.99</p></div>
  <div class="item" style="left:909px;top:478px;width:115px"><h3>Chicken Quesadilla</h3><p class="desc">Fajita seasoned chicken, Jack &amp; cheddar cheese, all grilled in a 12" flour tortilla with salsa &amp; sour cream</p><p class="price">9.99</p></div>

  <p class="brand" style="left:902px;top:545px">Salon Vireau</p>
</main>
</body>
</html>
```